Business Cards that are elegant and wow

I want to create and print business cards that represent my brand and stand out from the rest. We want to ensure they stay in our branding and the integrity is not lost. I am happy to look at different shapes like square etc.

It will be printed on very thick cards and will be stylish .

I want to create and print business cards that represent my brand and stand out from the rest. We want to ensure they stay in ur branding and the integrity is not lost. I am happy to look at different shapes like square etc.

Target Market(s)

real estate professionals

Industry/Entity Type

Real Estate

Contact Information for Business Card

Wren Holt
hello@bramblecovehomes.com.au
bramblecovehomes.com.au
0417 382 906 (SMS)

Colors

Designer to choose colors to be used in the design.

Requirements
Must have
• My logo
• email
• website
• Name
Nice to have
• I like the idea of printing with foil or spot gloss. You want it to stand out in a sea.
Should not have
• I would like you to stay in my colour themes. Don't change the colour of my logo

```html
<!DOCTYPE html>
<html lang="en">
<head>
<meta charset="utf-8">
<title>Bramble Cove Homes – Business Cards</title>
<link rel="stylesheet" href="https://fonts.googleapis.com/css2?family=Montserrat:wght@300;400;600&display=swap">
<style>
  :root {
    --backdrop: #a8acac;
    --card: #f4f4f2;
    --card-edge: #1a86d6;
    --brand-blue: #1f93dc;
    --brand-pink: #d81b60;
    --ink-grey: #6f6f6f;
  }
  * { margin: 0; padding: 0; box-sizing: border-box; }
  html, body {
    width: 1200px;
    height: 787px;
    overflow: hidden;
    background: var(--backdrop);
    font-family: "Montserrat", sans-serif;
  }
  .stage {
    position: relative;
    width: 1200px;
    height: 787px;
    display: flex;
    align-items: center;
    justify-content: center;
    gap: 60px;
  }
  .card {
    width: 500px;
    height: 300px;
    background: var(--card);
    border-bottom: 5px solid var(--card-edge);
    border-right: 3px solid var(--card-edge);
    box-shadow: 0 14px 28px rgba(0,0,0,0.18);
    position: relative;
  }
  .card--contact {
    display: flex;
    flex-direction: column;
    align-items: center;
    justify-content: center;
    gap: 6px;
  }
  .contact-name {
    font-weight: 600;
    font-size: 24px;
    letter-spacing: 1.5px;
    color: var(--brand-blue);
    text-transform: uppercase;
    margin-bottom: 6px;
  }
  .contact-icon {
    width: 14px;
    height: 14px;
    display: block;
  }
  .contact-line {
    font-weight: 300;
    font-size: 15px;
    letter-spacing: 0.6px;
    color: var(--ink-grey);
  }
  .card--brand {
    display: flex;
    align-items: center;
    justify-content: center;
    gap: 16px;
  }
  .brand-circle {
    width: 58px;
    height: 58px;
    flex: none;
  }
  .brand-name {
    font-weight: 600;
    font-size: 30px;
    letter-spacing: 1px;
    color: var(--brand-blue);
    text-transform: uppercase;
    line-height: 1;
  }
</style>
</head>
<body>
<main class="stage">
  <section class="card card--contact">
    <h1 class="contact-name">Wren Holt</h1>
    <svg class="contact-icon" viewBox="0 0 24 24" aria-hidden="true">
      <path fill="var(--brand-blue)" d="M6.6 10.8a15.1 15.1 0 0 0 6.6 6.6l2.2-2.2a1 1 0 0 1 1-.25 11.4 11.4 0 0 0 3.6.57 1 1 0 0 1 1 1V20a1 1 0 0 1-1 1A17 17 0 0 1 3 4a1 1 0 0 1 1-1h3.5a1 1 0 0 1 1 1c0 1.25.2 2.45.57 3.57a1 1 0 0 1-.25 1z"/>
    </svg>
    <p class="contact-line">0417 382 906</p>
    <svg class="contact-icon" viewBox="0 0 24 24" aria-hidden="true">
      <rect x="2" y="5" width="20" height="14" rx="1.5" fill="var(--brand-blue)"/>
      <path d="M3 6l9 7 9-7" fill="none" stroke="#ffffff" stroke-width="1.6"/>
    </svg>
    <p class="contact-line">hello@bramblecovehomes.com.au</p>
    <svg class="contact-icon" viewBox="0 0 24 24" aria-hidden="true">
      <circle cx="12" cy="12" r="10" fill="var(--brand-blue)"/>
      <path d="M2 12h20M12 2c3 3 3 17 0 20M12 2c-3 3-3 17 0 20" fill="none" stroke="#ffffff" stroke-width="1.3"/>
    </svg>
    <p class="contact-line">www.bramblecovehomes.com.au</p>
  </section>

  <section class="card card--brand">
    <svg class="brand-circle" viewBox="0 0 60 60" aria-hidden="true">
      <circle cx="30" cy="30" r="26" fill="none" stroke="var(--brand-pink)" stroke-width="4"/>
    </svg>
    <p class="brand-name">Bramble Cove Homes</p>
  </section>
</main>
</body>
</html>
```